K7 Maplewave Consulting Group Ltd - Website Design

We already have a company logo. We need a website created for our consulting agency.
Refer to attached files for logo and website content.
We would also be open to any additional recommendations.
Industry/Entity Type
Finance And Accounting
Coding
Coded - Design and coding required
Number of Pages Required
1 page
Font styles to use
Serif
Colors
3377b5
b868aa
33b8a4
Requirements
Must have
- Company Logo, name and who we are.

```html
<!DOCTYPE html>
<html lang="en">
<head>
<meta charset="utf-8">
<title>K7 Maplewave Consulting Group Ltd</title>
<link href="https://fonts.googleapis.com/css2?family=Roboto:wght@300;400;500;700&display=swap" rel="stylesheet">
<style>
:root{
  --brand-purple:#3d1a6e;
  --deep-violet:#2e0f63;
  --blue:#3377b5;
  --pink:#b868aa;
  --teal:#33b8a4;
  --panel:#efefef;
  --ink:#222;
  --muted:#666;
  --footer:#232323;
}
*{box-sizing:border-box;margin:0;padding:0}
html,body{width:1200px;height:2986px;overflow:hidden}
body{font-family:"Roboto",sans-serif;color:var(--ink);background:#fff;position:relative}
ul{list-style:none}

/* header */
.site-header{position:absolute;top:0;left:0;width:1200px;height:88px;background:#fff;z-index:3}
.brand{position:absolute;left:90px;top:24px;display:flex;align-items:center;gap:10px;font-size:24px;font-weight:400;color:var(--brand-purple);letter-spacing:.5px}
.brand-dot{width:26px;height:26px;border-radius:50%;background:var(--brand-purple)}
.main-nav a{position:absolute;top:36px;font-size:15px;letter-spacing:1px;color:var(--ink);text-decoration:none;font-weight:400;display:flex;align-items:center;gap:4px}
.main-nav a.active{color:var(--brand-purple);font-weight:500}
.main-nav .login{color:#6c5b88;font-weight:500}
.main-nav .signup{color:var(--brand-purple);font-weight:700}

/* hero */
.hero{position:absolute;top:88px;left:0;width:1200px;height:692px}
.hero-band{position:absolute;inset:0}
.hero-photo{position:absolute;inset:0;clip-path:polygon(0 0,1200px 0,1200px 613px,603px 683px,0 613px);
  background:radial-gradient(ellipse at 72% 40%,#1d4f7c 0%,transparent 45%),
  radial-gradient(ellipse at 55% 70%,#3ad2e6 0%,transparent 30%),
  linear-gradient(100deg,#2f7fa8 0%,#3a8fb5 30%,#1f5f86 60%,#143a5e 100%)}
.hero-title{position:absolute;left:84px;top:182px;font-size:86px;font-weight:300;color:#fff;letter-spacing:6px;line-height:1}
.hero-sub{position:absolute;left:87px;top:278px;font-size:26px;font-weight:300;color:#fff}
.btn{display:inline-flex;align-items:center;justify-content:center;gap:8px;background:var(--teal);color:#fff;border-radius:24px;font-size:16px;letter-spacing:1px;font-weight:400}
.hero .btn{position:absolute;left:88px;top:346px;width:196px;height:45px}

/* intro */
.section-title{position:absolute;left:0;width:1200px;text-align:center;font-size:48px;font-weight:300;letter-spacing:2px;color:#111}
.intro-text{position:absolute;left:230px;width:740px;top:918px;text-align:center;font-size:17.5px;font-weight:300;line-height:27px;color:var(--muted)}

/* services */
.services{position:absolute;left:0;top:1141px;width:1200px}
.tile{position:absolute;padding:0}
.tile h3{font-size:34px;font-weight:300;letter-spacing:1.5px;line-height:40px}
.tile ul{margin-top:18px}
.tile li{position:relative;padding-left:20px;font-size:15.5px;letter-spacing:.6px;line-height:27px}
.tile li::before{content:"›";position:absolute;left:0;top:1px;font-size:18px}
.tile-grey{background:var(--panel);color:#222}
.tile-blue{background:var(--blue);color:#fff}
.tile-teal{background:var(--teal);color:#fff}
.tile-pink{background:var(--pink);color:#fff}
.tile p{margin-top:18px;font-size:15.5px;letter-spacing:.6px;line-height:27px}
.photo{position:absolute}
.photo h3{position:absolute;left:46px;top:60px;color:#fff;font-size:34px;font-weight:300;letter-spacing:1.5px}

/* contact */
.contact h4{position:absolute;font-size:28px;font-weight:300;letter-spacing:1.5px}
.contact-copy{position:absolute;left:90px;top:2474px;width:405px;font-size:16px;font-weight:300;line-height:27px;text-align:justify;color:#333}
.contact-item{position:absolute;top:2625px;display:flex;align-items:center;gap:16px}
.contact-icon{width:52px;height:52px;border-radius:50%;border:2px solid var(--teal);display:flex;align-items:center;justify-content:center}
.contact-item small{display:block;font-size:14px;color:var(--brand-purple)}
.contact-item span{display:block;font-size:15.5px;color:#222;margin-top:4px}
.field{position:absolute;border:1px solid #cfcfcf;border-radius:25px;height:49px;width:257px;padding:0 24px;display:flex;align-items:center;font-size:15px;letter-spacing:.6px;color:#888}
.field.message{height:112px;width:521px;align-items:flex-start;padding-top:16px;border-radius:28px}
.contact .btn{position:absolute;left:590px;top:2722px;width:196px;height:47px}

/* footer */
.site-footer{position:absolute;left:0;top:2864px;width:1200px;height:122px;background:var(--footer);color:#fff}
.footer-nav{position:absolute;top:36px;left:0;width:1200px;display:flex;justify-content:center;gap:36px;font-size:15.5px}
.copyright{position:absolute;top:76px;width:1200px;text-align:center;font-size:13.5px}
</style>
</head>
<body>

<header class="site-header">
  <div class="brand"><span class="brand-dot"></span>K7 Maplewave</div>
  <nav class="main-nav">
    <a class="active" style="left:390px">HOME</a>
    <a style="left:479px">WHO WE ARE</a>
    <a style="left:621px">SERVICES OFFERED
      <svg width="10" height="7" viewBox="0 0 10 7"><path d="M1 1l4 4 4-4" fill="none" stroke="#222" stroke-width="1.3"/></svg></a>
    <a style="left:824px">CONTACT US</a>
    <a class="login" style="left:973px">LOGIN</a>
    <a class="signup" style="left:1045px">SIGN UP</a>
  </nav>
</header>

<section class="hero">
  <svg class="hero-band" width="1200" height="692" aria-hidden="true">
    <polygon points="603,683 1200,613 1200,650 690,692" fill="var(--deep-violet)"/>
  </svg>
  <div class="hero-photo" role="img" aria-label="Business person pointing at glowing financial charts and figures"></div>
  <h1 class="hero-title">K7 MAPLEWAVE</h1>
  <p class="hero-sub">Consulting Group LTD</p>
  <a class="btn">GET STARTED <span>»</span></a>
</section>

<h2 class="section-title" style="top:856px">Who we are</h2>
<p class="intro-text">We are a boutique Financial Management Agency that provides specialized services for small and medium sized enterprises</p>

<h2 class="section-title" style="top:1056px">Services Offered</h2>

<section class="services">
  <!-- row 1 -->
  <div class="tile tile-grey" style="left:0;top:0;width:424px;height:345px;padding:60px 0 0 46px">
    <h3>Accounting</h3>
    <ul>
      <li>Preparation of financial reports</li>
      <li>Regulatory compliance</li>
      <li>Compensation planning</li>
      <li>Corporate tax consulting</li>
      <li>Accounting system implementation and migrations</li>
    </ul>
  </div>
  <div class="tile tile-blue" style="left:424px;top:0;width:425px;height:345px;padding:60px 40px 0 47px">
    <h3>Government Grants</h3>
    <p>Process applications for government grants and tax breaks</p>
  </div>
  <div class="photo" role="img" aria-label="Hands working on a calculator beside financial reports" style="left:849px;top:0;width:351px;height:345px;background:linear-gradient(135deg,#6f7478 0%,#a9adb0 45%,#d7d8d6 70%,#8e7a3c 100%)">
    <h3>Bookkeeping</h3>
  </div>

  <!-- row 2 -->
  <div class="photo" role="img" aria-label="Business meeting with documents and a calculator on a desk" style="left:0;top:345px;width:637px;height:425px;background:linear-gradient(160deg,#c9d3de 0%,#e6eaee 45%,#f4f4f2 75%,#c9c9c7 100%)"></div>
  <div class="tile tile-teal" style="left:0;top:345px;width:268px;height:259px;padding:48px 0 0 37px">
    <h3>Mergers and Acquisitions</h3>
    <ul style="margin-top:12px">
      <li>Operations due diligence</li>
      <li>Integration services</li>
    </ul>
  </div>
  <div class="tile tile-grey" style="left:637px;top:345px;width:563px;height:425px;padding:48px 0 0 61px">
    <h3>Financial Management</h3>
    <ul>
      <li>Cash flow management</li>
      <li>Financial and management reporting</li>
      <li>Budgeting and forecasting</li>
      <li>Technical accounting advisory</li>
      <li>Business plan preparation</li>
      <li>Finance process improvements</li>
      <li>Governance</li>
      <li>Secure financing</li>
      <li>Lease accounting</li>
      <li>Expense management</li>
    </ul>
  </div>

  <!-- row 3 -->
  <div class="tile tile-pink" style="left:0;top:770px;width:424px;height:345px;padding:42px 0 0 46px">
    <h3>Internal Audit<br>(or Assurance)</h3>
    <ul style="padding-right:10px">
      <li>Audit and review of financial and non-financial information</li>
      <li>Internal control reviews</li>
      <li>Assessment of Business Risk</li>
      <li>Review of suppliers</li>
      <li>Viability reviews</li>
    </ul>
  </div>
  <div class="tile tile-grey" style="left:424px;top:770px;width:425px;height:345px;padding:38px 0 0 46px">
    <h3>Strategy</h3>
    <ul>
      <li>Operational governance</li>
      <li>Market research</li>
      <li>Sales &amp; marketing analysis</li>
      <li>Growth strategies</li>
      <li>Decision management</li>
      <li>Operations optimization</li>
      <li>Third party vendor assessments</li>
      <li>Systems transformations</li>
    </ul>
  </div>
  <div class="photo" role="img" aria-label="Team reviewing charts and sticky notes on a wooden table" style="left:849px;top:770px;width:351px;height:345px;background:linear-gradient(150deg,#4a4a4c 0%,#8a8580 40%,#c9b79a 70%,#e3d6c2 100%)"></div>
</section>

<section class="contact">
  <h2 class="section-title" style="top:2336px">Contact Us</h2>
  <h4 style="left:88px;top:2424px">Let’s Talk</h4>
  <h4 style="left:589px;top:2424px">Get In Touch</h4>
  <p class="contact-copy">Lorem ipsum dolor sit amet, consectetur adipiscing elit, sed do eiusmod tempor incididunt ut labore et dolore magna aliqua. Ut enim ad minim veniam, quis nostrud exercitation ullamco laboris nisi ut aliquip ex ea commodo consequat.</p>
  <div class="contact-item" style="left:91px">
    <div class="contact-icon"><svg width="16" height="16" viewBox="0 0 24 24"><path d="M6.6 10.8a15 15 0 006.6 6.6l2.2-2.2c.3-.3.7-.4 1-.2 1.1.4 2.3.6 3.6.6.6 0 1 .4 1 1V20c0 .6-.4 1-1 1C10.6 21 3 13.4 3 4c0-.6.4-1 1-1h3.5c.6 0 1 .4 1 1 0 1.3.2 2.5.6 3.6.1.3 0 .7-.2 1z" fill="var(--teal)"/></svg></div>
    <div><small>Call Us :</small><span>+8 888 888 888</span></div>
  </div>
  <div class="contact-item" style="left:306px">
    <div class="contact-icon"><svg width="16" height="13" viewBox="0 0 16 13"><rect x="0" y="0" width="16" height="13" rx="1.5" fill="var(--teal)"/><path d="M1 1.5l7 5.5 7-5.5" fill="none" stroke="#fff" stroke-width="1.4"/></svg></div>
    <div><small>Email Us :</small><span style="font-size:14.5px">hello@k7maplewave.com</span></div>
  </div>

  <form>
    <div class="field" style="left:590px;top:2484px">Name</div>
    <div class="field" style="left:854px;top:2484px">Email</div>
    <div class="field" style="left:590px;top:2543px">Phone no</div>
    <div class="field" style="left:854px;top:2543px">Company</div>
    <div class="field message" style="left:590px;top:2602px">Message</div>
    <a class="btn">SUBMIT <span style="margin-left:24px">»</span></a>
  </form>
</section>

<footer class="site-footer">
  <nav class="footer-nav"><span>Home</span><span>Who we are</span><span>Services offered</span><span>Contact Us</span></nav>
  <p class="copyright">© Copyrights.2021.The Company name</p>
</footer>

</body>
</html>
```